BKA

Please send us some options for letterhead I attached our Logo. In addition to the Logo we need this information somewhere on the page

47 Fenbury Lane
Norbrook, CT 06742
203-481-7629

```html
<!DOCTYPE html>
<html lang="en">
<head>
<meta charset="utf-8">
<title>BKA Stationery</title>
<link rel="stylesheet" href="https://fonts.googleapis.com/css2?family=Arimo:wght@400;700&display=swap">
<style>
  :root {
    --stage: #e8e9eb;
    --paper: #ffffff;
    --ink: #4d4843;
    --text: #2b2b2b;
    --blue-deep: #1b6fae;
    --blue-light: #5fc0e6;
    --shadow: rgba(0, 0, 0, 0.28);
  }
  * { margin: 0; padding: 0; box-sizing: border-box; }
  html, body {
    width: 1200px;
    height: 900px;
    overflow: hidden;
    background: var(--stage);
    font-family: "Arimo", Arial, sans-serif;
  }
  .canvas { position: relative; width: 1200px; height: 900px; }

  .sheet {
    position: absolute;
    background: var(--paper);
    box-shadow: 2px 4px 8px var(--shadow);
  }
  .letterhead { left: 75px; top: 28px; width: 595px; height: 840px; }
  .envelope { left: 543px; top: 225px; width: 596px; height: 265px; }

  .band {
    position: absolute;
    left: 0;
    width: 100%;
    background: linear-gradient(90deg, var(--blue-deep) 0%, var(--blue-deep) 20%, var(--blue-light) 50%, var(--blue-deep) 82%, var(--blue-deep) 100%);
  }
  .band-top { top: 0; height: 6px; }
  .band-bottom { bottom: 0; height: 8px; }

  .brand {
    position: absolute;
    display: flex;
    align-items: center;
    gap: 10px;
    color: var(--ink);
    font-weight: 700;
    letter-spacing: 1px;
    white-space: nowrap;
  }
  .brand-mark { background: var(--ink); flex: none; }

  .letterhead .brand { left: 62px; top: 18px; font-size: 40px; }
  .letterhead .brand-mark { width: 62px; height: 62px; }

  .envelope .brand { left: 42px; top: 18px; font-size: 40px; }
  .envelope .brand-mark { width: 62px; height: 62px; }

  .brand-standalone { left: 783px; top: 626px; font-size: 56px; gap: 14px; }
  .brand-standalone .brand-mark { width: 86px; height: 86px; }

  .contact {
    position: absolute;
    left: 444px;
    top: 43px;
    font-size: 9.5px;
    line-height: 12px;
    color: var(--text);
    font-style: normal;
    white-space: nowrap;
  }
</style>
</head>
<body>
<main class="canvas">
  <section class="sheet letterhead" aria-label="Letterhead">
    <div class="band band-top"></div>
    <div class="brand"><span class="brand-mark"></span><span class="brand-name">BKA</span></div>
    <address class="contact">
      47 Fenbury Lane<br>
      Norbrook, CT 06742<br>
      203-481-7629
    </address>
    <div class="band band-bottom"></div>
  </section>

  <section class="sheet envelope" aria-label="Envelope">
    <div class="brand"><span class="brand-mark"></span><span class="brand-name">BKA</span></div>
    <div class="band band-bottom"></div>
  </section>

  <div class="brand brand-standalone"><span class="brand-mark"></span><span class="brand-name">BKA</span></div>
</main>
</body>
</html>
```